Business start up

I need a logo within the business cards that has the name brontz with two racing stripes like the vexor racing stripes next to the name .... one of the stripes I would want to have the shades of window tint and the other stripe the colors of vinyl wrap or even the name having dripping paint of the different colors in it ... it will be a business of window tint and vinyl wrap .... service that I will be providing would be window tint Vinyl wrap Paint protection (ppfTaillights/headlights tintsBlackouts/Chrome delete Decals

Target Market(s)

Automotive

Industry/Entity Type

Automotive

Contact Information for Business Card

Have the name brontz drip like paint and have different colors dripping

Font styles to use
Serif
Sans Serif
Decorative
Script

Colors

Designer to choose colors to be used in the design.

Requirements
Nice to have
• I need a logo within the business cards that has the name brontz with two racing stripes like the vexor racing stripes next to the name .... one of the stripes I would want to have the shades of window tint and the other stripe the colors of vinyl wrap or even the name having dripping paint of the different colors in it ... it will be a business of window tint and vinyl wrap .... service that I will be providing would be
• window tint
• Vinyl wrap
• Paint protection (ppf
• Taillights/headlights tints
• Blackouts/Chrome delete
• Decals

```html
<!DOCTYPE html>
<html lang="en">
<head>
<meta charset="utf-8">
<title>Brontz business cards</title>
<link href="https://fonts.googleapis.com/css2?family=Open+Sans:wght@400;600&display=swap" rel="stylesheet">
<style>
  :root{
    --backdrop:#e6e7ea;
    --card:#ffffff;
    --ink:#1a1a1a;
    --accent:#e24f22;
    --blush:#fbeeed;
    --grey-light:#e6e6e6;
    --grey-mid:#cfcfcf;
    --butter:#fbf8d8;
    --lilac:#ddd4ea;
    --rose:#f2cccc;
  }
  *{margin:0;padding:0;box-sizing:border-box}
  html,body{width:1200px;height:900px;overflow:hidden}
  body{background:var(--backdrop);font-family:"Open Sans",Arial,sans-serif;color:var(--ink);position:relative}

  .card{position:absolute;top:295px;width:540px;height:310px;background:var(--card);border-radius:18px;overflow:hidden;box-shadow:0 10px 30px rgba(0,0,0,.15)}
  .card--back{left:40px}
  .card--front{left:620px}

  .brand{position:absolute;display:flex;align-items:center;gap:10px;font-weight:600;letter-spacing:.06em;color:var(--ink);line-height:1}
  .brand__square{width:16px;height:16px;background:var(--accent)}
  .card--back .brand{left:200px;top:20px;font-size:30px}
  .card--front .brand{left:40px;top:96px;font-size:40px}

  .services{position:absolute;left:26px;top:64px;list-style:none;font-size:13px;line-height:1.4}
  .services li::before{content:"\25B8";font-size:11px;margin-right:8px}

  .tint-band{position:absolute;left:0;right:0;top:184px;height:28px;background:linear-gradient(90deg,var(--grey-light),var(--grey-mid))}
  .wrap-band{position:absolute;left:0;top:226px;width:300px;bottom:0;background:linear-gradient(90deg,var(--butter),var(--lilac),var(--rose))}

  .contact{position:absolute;left:330px;top:224px;font-size:14px;line-height:1.35}

  .blush-band{position:absolute;left:0;right:0;top:180px;bottom:0;background:linear-gradient(180deg,rgba(251,238,237,0),var(--blush) 40%)}
</style>
</head>
<body>
  <section class="card card--back">
    <div class="brand"><span class="brand__square"></span>BRONTZ</div>
    <ul class="services">
      <li>window tint</li>
      <li>Vinyl wrap</li>
      <li>Paint protection (ppf)</li>
      <li>Taillights/headlights tints</li>
      <li>Blackouts/Chrome delete</li>
      <li>Decals</li>
    </ul>
    <div class="tint-band" role="img" aria-label="Decorative band of window tint shades"></div>
    <div class="wrap-band" role="img" aria-label="Decorative band of vinyl wrap colours"></div>
    <div class="contact">
      <p>Your Name</p>
      <p>Contact No</p>
      <p>Address</p>
      <p>Email</p>
    </div>
  </section>

  <section class="card card--front">
    <div class="blush-band" role="img" aria-label="Soft pale pink decorative stripes"></div>
    <div class="brand"><span class="brand__square"></span>BRONTZ</div>
  </section>
</body>
</html>
```